R.K Landscaping 484-883-7758Mulching Mowing Planting Spring and Fall Clean up

The colors I would like to work with Are black and green.I do have a Facebook page it's https://www.vernetsocial.example/RK-Landscaping-902145638870214/

For my business logo I would like to put that either on the corner or in the background

Services: mowing, mulching, fall and spring cleanup, hedge trimming

Requirements
Must have
• Please use these pics
• I like Design #9926064
• and room for addresses to
Should not have
• the pics in the back of card

```html
<!DOCTYPE html>
<html lang="en">
<head>
<meta charset="utf-8">
<title>R.K Landscaping – Business Card</title>
<link rel="stylesheet" href="https://fonts.googleapis.com/css2?family=Josefin+Sans:wght@300;400;700&family=Libre+Baskerville:ital@1&display=swap">
<style>
  :root {
    --page-bg: #e6e2da;
    --leaf-green: #8cc63f;
    --white: #ffffff;
    --bark-dark: #2a211b;
    --bark-mid: #5a4636;
    --bamboo: #8a8a4a;
    --card-shadow: rgba(0, 0, 0, 0.18);
  }
  * { box-sizing: border-box; margin: 0; padding: 0; }
  html, body {
    width: 1200px;
    height: 801px;
    overflow: hidden;
    background: var(--page-bg);
    font-family: "Josefin Sans", sans-serif;
  }
  .card {
    position: absolute;
    top: 252px;
    width: 520px;
    height: 297px;
    overflow: hidden;
    box-shadow: 0 4px 14px var(--card-shadow);
  }
  .card--front { left: 60px; }
  .card--back { left: 620px; background: var(--leaf-green); }

  /* Front */
  .front-photo {
    position: absolute;
    inset: 0;
    background:
      linear-gradient(90deg, rgba(42,33,27,0.55) 0%, rgba(42,33,27,0) 45%),
      linear-gradient(100deg, var(--bark-mid) 0%, var(--bark-dark) 40%, var(--bamboo) 75%, var(--bark-mid) 100%);
  }
  .front-brand {
    position: absolute;
    left: 150px;
    top: 72px;
    width: 230px;
    text-align: center;
    color: var(--white);
  }
  .brand-dot {
    display: block;
    width: 44px;
    height: 44px;
    margin: 0 auto 8px;
    border-radius: 50%;
    background: var(--white);
  }
  .brand-name {
    font-weight: 700;
    font-size: 24px;
    letter-spacing: 0.5px;
    text-transform: uppercase;
  }
  .brand-tagline {
    font-family: "Libre Baskerville", serif;
    font-style: italic;
    font-size: 11px;
    margin-top: 4px;
  }
  .brand-phone {
    font-weight: 700;
    font-size: 22px;
    margin-top: 8px;
  }
  .front-services {
    position: absolute;
    left: 0;
    right: 0;
    bottom: 30px;
    text-align: center;
    color: var(--white);
    font-weight: 700;
    font-size: 11px;
    letter-spacing: 0.3px;
    text-transform: uppercase;
  }

  /* Back */
  .back-brand {
    position: absolute;
    top: 14px;
    right: 26px;
    width: 120px;
    text-align: center;
    color: var(--white);
  }
  .back-brand .brand-dot { width: 28px; height: 28px; margin-bottom: 5px; }
  .back-brand .brand-name { font-size: 13px; }
  .back-brand .brand-phone { font-size: 12px; margin-top: 3px; }
  .back-services {
    position: absolute;
    left: 28px;
    top: 118px;
    color: var(--white);
    text-transform: uppercase;
    line-height: 1.02;
  }
  .service { display: block; font-size: 33px; }
  .service--bold { font-weight: 700; }
  .service--light { font-weight: 300; }
</style>
</head>
<body>
  <section class="card card--front">
    <div class="front-photo" role="img" aria-label="Photo of a wooden fence with bamboo stalks"></div>
    <div class="front-brand">
      <span class="brand-dot"></span>
      <p class="brand-name">R.K Landscaping</p>
      <p class="brand-tagline">For all your Professional Landscaping Needs</p>
      <p class="brand-phone">312-555-0194</p>
    </div>
    <p class="front-services">Mowing, Mulching, Fall and Spring Cleanup, Hedge Trimming</p>
  </section>

  <section class="card card--back">
    <div class="back-brand">
      <span class="brand-dot"></span>
      <p class="brand-name">R.K Landscaping</p>
      <p class="brand-phone">312-555-0194</p>
    </div>
    <div class="back-services">
      <span class="service service--bold">Mowing,</span>
      <span class="service service--light">Mulching,</span>
      <span class="service service--bold">Fall &amp; Spring Cleanup,</span>
      <span class="service service--light">Hedge Trimming</span>
    </div>
  </section>
</body>
</html>
```